GLS biz card

We need a business card design for our new company based in Los Angeles called "Gold Lantern Studios". We develop film and television projects. We work with investors, financiers, film production companies, film distribution and sales companies as well as studios. We would like to incorporate our logo (see attached) on a two-sided card. We need to include: name and title, address, phone, email and company website.

Target Market(s)

Business, financial and studio clients

Industry/Entity Type

Business

Contact Information for Business Card

Two-sided. We are thinking of the logo on one side and the information on the back. Please feel free to be creative! Thanks.

Requirements
Must have
• Please include the following text information, excluding the "CAPS CATEGORY:" and please allow the ability for us to change the name, title and email address for each company employee):
• NAME & TITLE:
• Peter Dunmore
• Managing Partner
• COMPANY NAME:
• GOLD LANTERN STUDIOS (please use existing logo)
• COMPANY ADDRESS:
• KVT Arts Park
• 2480 Wexley Boulevard
• Arts Hall, 4th Floor
• Manhattan Beach, CA 90266
• COMPANY PHONE NUMBER:
• 310-555-4206
• COMPANY WEBSITE ADDRESS:
• www.goldlanternstudioshouse.com
• EMAIL ADDRESS: (only one per card)
• frank@goldlanternstudioshouse.com
• tizzy@goldlanternstudioshouse.com
• peter@goldlanternstudioshouse.com

```html
<!DOCTYPE html>
<html lang="en">
<head>
<meta charset="utf-8">
<title>Gold Lantern Studios – Business Card</title>
<link href="https://fonts.googleapis.com/css2?family=Ubuntu:wght@400;500;700&display=swap" rel="stylesheet">
<style>
  :root {
    --stage: #1c1c1e;
    --card: #5b5c5e;
    --card-light: #67686a;
    --card-dark: #4c4d4f;
    --brand-blue: #2a86a3;
    --brand-blue-deep: #1b5d74;
    --dot-blue: #2f6e82;
    --ink-dark: #164b60;
    --text-light: #ffffff;
    --text-soft: #d9dde0;
    --stripe: #1f5568;
  }
  * { box-sizing: border-box; margin: 0; padding: 0; }
  html, body {
    width: 1200px; height: 992px; overflow: hidden;
    background: var(--stage);
    font-family: "Ubuntu", Arial, sans-serif;
  }
  .canvas {
    width: 1200px; height: 992px;
    display: flex; align-items: center; justify-content: center; gap: 40px;
  }
  .card {
    position: relative;
    width: 540px; height: 309px;
    background: linear-gradient(160deg, var(--card-light), var(--card) 45%, var(--card-dark));
    overflow: hidden;
    box-shadow: 0 10px 30px rgba(0,0,0,.5);
  }

  /* Contact side */
  .pattern-area {
    position: absolute; right: 0; top: 0;
    width: 62%; height: 58%;
    background: radial-gradient(ellipse at 85% 10%, rgba(47,110,130,.75), rgba(47,110,130,.35) 55%, rgba(47,110,130,0) 80%);
  }
  .name-band {
    position: absolute; left: 0; top: 92px;
    width: 250px; height: 54px;
    background: var(--brand-blue);
    border-radius: 0 4px 4px 0;
    padding: 6px 0 0 20px;
  }
  .name {
    font-size: 24px; font-weight: 700; line-height: 1;
    color: var(--text-light);
  }
  .name .first { color: var(--ink-dark); }
  .job-title {
    font-size: 12px; color: var(--text-light); margin-top: 4px; letter-spacing: .3px;
  }
  .contact-list {
    position: absolute; left: 20px; top: 160px;
    list-style: none;
  }
  .contact-list li {
    display: flex; align-items: flex-start; gap: 9px;
    font-size: 11px; line-height: 16px; color: var(--text-light);
    margin-bottom: 7px;
  }
  .contact-list .icon {
    flex: none;
    width: 16px; height: 16px; border-radius: 4px;
    background: var(--brand-blue);
    display: flex; align-items: center; justify-content: center;
  }
  .contact-list .address span { display: block; }

  /* Logo side */
  .stripes {
    position: absolute; top: 0; bottom: 0; width: 14px;
    border-left: 2px solid var(--stripe);
    border-right: 2px solid var(--stripe);
  }
  .stripes.left { left: 22px; }
  .stripes.right { right: 22px; }
  .brand {
    position: absolute; left: 0; right: 0; top: 48px;
    display: flex; flex-direction: column; align-items: center;
  }
  .brand-mark {
    width: 112px; height: 112px; border-radius: 50%;
    background: var(--brand-blue-deep);
    margin-bottom: 22px;
  }
  .brand-name {
    font-size: 24px; font-weight: 500; letter-spacing: 3px;
    color: var(--brand-blue);
  }
  .brand-tagline {
    margin-top: 8px;
    font-size: 9px; letter-spacing: 2.6px;
    color: var(--text-soft);
  }
</style>
</head>
<body>
<main class="canvas">

  <section class="card card-info" aria-label="Business card, contact side">
    <div class="pattern-area" role="img" aria-label="Decorative perspective dot pattern in teal on grey"></div>
    <div class="name-band">
      <p class="name"><span class="first">Peter</span> Dunmore</p>
      <p class="job-title">Managing Partner</p>
    </div>
    <ul class="contact-list">
      <li>
        <span class="icon">
          <svg width="10" height="8" viewBox="0 0 10 8"><rect x=".5" y=".5" width="9" height="7" fill="none" stroke="#fff"/><path d="M.5 .5 5 4.5 9.5 .5" fill="none" stroke="#fff"/></svg>
        </span>
        peter@goldlanternstudioshouse.com
      </li>
      <li>
        <span class="icon">
          <svg width="7" height="10" viewBox="0 0 7 10"><rect x=".5" y=".5" width="6" height="9" rx="1" fill="none" stroke="#fff"/><circle cx="3.5" cy="7.6" r=".8" fill="#fff"/></svg>
        </span>
        310-555-4206
      </li>
      <li>
        <span class="icon">
          <svg width="10" height="10" viewBox="0 0 10 10" fill="none" stroke="#fff" stroke-width=".9"><circle cx="5" cy="5" r="4.3"/><ellipse cx="5" cy="5" rx="2" ry="4.3"/><path d="M.7 5h8.6"/></svg>
        </span>
        www.goldlanternstudioshouse.com
      </li>
      <li class="address">
        <span class="icon">
          <svg width="8" height="10" viewBox="0 0 8 10"><path d="M4 9.5C1.5 6.5.5 5 .5 3.6a3.5 3.5 0 0 1 7 0C7.5 5 6.5 6.5 4 9.5z" fill="#fff"/><circle cx="4" cy="3.6" r="1.3" fill="#2a86a3"/></svg>
        </span>
        <p>
          <span>KVT Arts Park, 2480 Wexley Boulevard</span>
          <span>Arts Hall, 4th Floor</span>
          <span>Manhattan Beach, CA 90266</span>
        </p>
      </li>
    </ul>
  </section>

  <section class="card card-brand" aria-label="Business card, logo side">
    <div class="stripes left"></div>
    <div class="stripes right"></div>
    <div class="brand">
      <div class="brand-mark"></div>
      <p class="brand-name">GOLD LANTERN STUDIOS</p>
      <p class="brand-tagline">A MEDIA ENTERTAINMENT COMPANY</p>
    </div>
  </section>

</main>
</body>
</html>
```